A professional business to business web site for a contract agency called VONTAREX.

We need a very clean, very professional web site created for business to business. It is an informational web site with 3 pages. We are a company that offers contract employee placements into primarily the pharmaceutical industry. I have attached a file that describes the company more fully.

Hi,

I'm sorry if I wasn't clear, but I need to have the HTML pages created so I can just upload the files you give me to the web hosting site.

Please let me know if you have any questions.

Thanks for working on my project!

Hello,

I didn't put this in the description, but I would need the web site set up on the web hosting site as well.  The web hosting site is abrightkettle.  I want a copy of all the files as well.

Thanks,
Miles

Reason: I'm sorry, unexpectedly, I have been very busy and I haven't been able to devote the time necessary for this. I am extending the deadline by 10 days. Thank you for your patience. Thanks.

Reason: Hi everyone, I apologize again, but everything has been so busy here that I haven't been able to give this attention. I plan to work on this over the next few days. Thanks and sorry again, Miles.

Reason: I'm sorry this is taking longer than planned. I have been extremely busy. I have increased the budget on this project. Thanks.

Target Market(s)

Large professional corporations mainly in the pharmaceutical industry. The audience is hiring decisions makers within the companies and potential job candidates/job seekers.

Industry/Entity Type

Pharmaceutical

Font styles to use
Sans Serif

Requirements
Must have
• Must have a clean look that mimics the pharmaceutical industry web sites. VERY professional.
Nice to have
• A nice picture of professional business/pharma/technical people looking like a team. Colors are listed on the attached Word document.
Should not have
• No animation. Not too busy.

```html
<!DOCTYPE html>
<html lang="en">
<head>
<meta charset="utf-8">
<title>VONTAREX — Contract Professionals</title>
<link rel="stylesheet" href="https://fonts.googleapis.com/css2?family=Lato:wght@300;400;700&display=swap">
<style>
  :root {
    --brand-blue: #0b4c9b;
    --brand-navy: #1b2a77;
    --field-blue: #1f78e8;
    --phone-blue: #3a8cf2;
    --ink: #1f1f1f;
    --white: #ffffff;
    --nav-active: rgba(62, 62, 62, 0.78);
    --hero-shade: rgba(38, 38, 40, 0.72);
  }
  * { box-sizing: border-box; margin: 0; padding: 0; }
  html, body { width: 1200px; height: 925px; overflow: hidden; background: var(--white); }
  body { position: relative; font-family: "Lato", Arial, sans-serif; color: var(--ink); }

  .brand { position: absolute; left: 36px; top: 38px; display: flex; align-items: center; gap: 9px; }
  .brand-dot { width: 20px; height: 20px; border-radius: 50%; background: var(--brand-navy); }
  .brand-name { font-family: "Lato", Arial, sans-serif; font-weight: 400; font-size: 15px; letter-spacing: 3px; color: var(--brand-navy); }

  .contact-strip { position: absolute; right: 19px; top: 28px; font-size: 15px; color: var(--brand-blue); }
  .contact-strip strong { color: #3a3a55; font-weight: 700; }

  .side-column { position: absolute; left: 813px; top: 57px; width: 387px; height: 868px; background: var(--brand-blue); }

  .call-us { position: absolute; right: 14px; top: 66px; color: var(--white); font-family: Arial, sans-serif; font-size: 17px; display: flex; align-items: baseline; gap: 12px; }
  .call-us .phone { font-size: 25px; font-weight: 700; color: var(--phone-blue); }

  .hero { position: absolute; left: 0; top: 118px; width: 1200px; height: 360px; }
  .hero-photo { position: absolute; inset: 0; background: linear-gradient(100deg, #c9d3db 0%, #e3e8ec 30%, #b9c3cc 55%, #5d6a78 80%, #7a6a5c 100%); }
  .hero-shade { position: absolute; left: 813px; top: 0; width: 387px; height: 100%; background: var(--hero-shade); }
  .hero-tagline { position: absolute; left: 840px; top: 52px; color: var(--white); font-family: Arial, sans-serif; font-size: 58px; line-height: 70px; text-transform: uppercase; }

  .main-nav { position: absolute; left: 0; top: 118px; height: 63px; display: flex; }
  .main-nav a { display: block; height: 63px; line-height: 62px; color: var(--white); text-decoration: none; font-weight: 300; font-size: 19px; }
  .main-nav .nav-home { padding-left: 34px; width: 200px; }
  .main-nav .nav-services { width: 232px; }
  .main-nav .nav-contact { width: 227px; padding-left: 50px; background: var(--nav-active); }

  .about { position: absolute; left: 36px; top: 550px; width: 750px; }
  .about h2 { font-weight: 300; font-size: 39px; color: var(--brand-blue); line-height: 46px; margin-bottom: 6px; }
  .about p { font-size: 18px; line-height: 24px; font-weight: 400; color: var(--ink); }

  .contact-form { position: absolute; left: 843px; top: 550px; width: 312px; }
  .contact-form h2 { font-weight: 300; font-size: 39px; line-height: 46px; color: var(--white); margin-bottom: 11px; }
  .field { display: block; width: 312px; height: 31px; background: var(--field-blue); border: 0; color: var(--brand-blue); font-family: Arial, sans-serif; font-size: 15px; padding: 5px 9px; margin-bottom: 16px; }
  .field-message { height: 93px; margin-bottom: 0; }
  .submit { display: block; margin-left: -1px; width: 135px; height: 46px; background: var(--brand-navy); color: var(--phone-blue); font-family: Arial, sans-serif; font-size: 16px; text-align: center; line-height: 46px; }

  .copyright { position: absolute; left: 37px; top: 887px; font-family: Arial, sans-serif; font-size: 12px; color: var(--ink); }
</style>
</head>
<body>
  <div class="side-column"></div>

  <header>
    <div class="brand"><span class="brand-dot"></span><span class="brand-name">VONTAREX</span></div>
    <div class="contact-strip"><strong>Email:</strong> contact.us@VONTAREX.com</div>
    <div class="call-us"><span>CALL US</span><span class="phone">555-014-0372</span></div>
  </header>

  <section class="hero">
    <div class="hero-photo" role="img" aria-label="Photo of a team of lab scientists looking together at a monitor"></div>
    <div class="hero-shade"></div>
    <p class="hero-tagline">Some<br>one-line<br>text<br>here</p>
  </section>

  <nav class="main-nav">
    <a class="nav-home" href="#">HOME</a>
    <a class="nav-services" href="#">SERVICES OFFERED</a>
    <a class="nav-contact" href="#">CONTACT US</a>
  </nav>

  <section class="about">
    <h2>ABOUT US</h2>
    <p>VONTAREX specializes in offering contract professionals primarily to companies in pharmaceu-<br>tical lab environments.&nbsp; We look for the top people and companies to work with.&nbsp; Whether you are looking for a position, or looking for a contractor, you have come to the right place.&nbsp; We work hard to put great team members together with great teams.</p>
  </section>

  <section class="contact-form">
    <h2>DROP US A LINE</h2>
    <div class="field">Name</div>
    <div class="field">Email</div>
    <div class="field field-message">Message</div>
    <div class="submit">SUBMIT</div>
  </section>

  <footer class="copyright">Copyright : Vontarex&nbsp; 2014</footer>
</body>
</html>
```